New doctor needs elegant, whimsical Business Card Design

CHALLENGE: how to highlight gynaecological service (use of abstract cervix in logo?) in NON-VULGAR way + project an elegant, professional tone?

We need a business card design (incl logo) for a gynaecologist who is starting his private practice. The main area of service will be colposcopy - a diagnostic procedure using a microscope to look at the tissues of the cervix for any potentially cancerous cells.

STYLE: Classic, elegant, timeless look. Fairly simple, not too cluttered. Logo NOT to overpower name. Want to project a professional but approachable image - "gentleman". Not too "corporate" - whimsical, without becoming feminine.

COLOUR: soft colours - no clashing primary colours, nothing too "brash" or commercial.
White background/black lettering + 1 colour accent, pattern repeated throughout card, in both logo & text (refer to "mock-up example" image file)
The colour accent should be BLUE: a serene/calm but confident shade: eg. strong pastel blue, dark baby blue (NOT royal blue, navy, turquoise, aquamarine, etc)

TEXT: have a calligraphy feel (but not too fancy as to be difficult to read at a glance) or more italics/rounded edges kind of font (refer to refer to "mock-up example" image file)
- Contrast between NAME in more italic font Vs. rest of text in "straight" print (or vice versa)

LOGO:
1) something very similar to "The Wren Trust" logo (ref image attached) - an abstract, black line drawing of a woman's figure, with a single, coloured symbol. No detail in line drawing - NO head or arms - don't want it to be obviously women's figure - want it very stylised, abstract, fluid lines.

* The Wren Trust used a heart but we would like to use an another symbol in BLUE - maybe an abstract of a cervix? eg. the "triangle" shape symbol (see the image file of the Silver Thread Wellness Initiative - the symbol in the middle of the flower) OR the "donut" representation of the cervix (see notes below)

BUT - don't want the symbol exactly over the groin area, otherwise looks vulgar. Don't want it to look like bikini or genitals! Symbol should be incorporated into line drawing but NOT drawing direct attention to the groin. Maybe displaced to one side? Or further up the body? Open to your ideas

2) We are also open to any other ideas you may have, of stylistic/abstract designs based on:
- the image of a cervix (looks very similar to a pink donut - usually shown in medical shorthand as a tiny circle in the middle of a bigger circle.)
- the cervix with some cells within ? Some stylised version of cancer cells?
(please see attached selection of images for reference/inspiration)

2 main audiences: women (18 - 70) concerned about abnormal PAP smear, other gynae-issues, 2) GP's referring their patients to a gynae-specialist

Medical

• ONE side only - Reverse of business card must be kept blank for "Appointments" notes.

• NO "retro" American feel - nor anything 60's or 70's kind of feel. Don't want fonts that look too commercial or industrial/harsh.

Logo: NO obvious silhouettes/profiles of women (abstract is OK but not detail), NO female reproductive system (2 ovaries & uterus), no female symbol - as these are the usual cliches for gynaecologists.

DON'T want the symbol exactly over the groin area, otherwise looks vulgar. Don't want it to look like bikini or genitals! Symbol should be incorporated into line drawing but NOT drawing direct attention to the groin. Maybe displaced to one side? Or further up the body? Open to your ideas

```html
<!DOCTYPE html>
<html lang="en">
<head>
<meta charset="utf-8">
<title>Dr. Martin Hale – Gynaecologist</title>
<link rel="stylesheet" href="https://fonts.googleapis.com/css2?family=Caveat+Brush&family=Sorts+Mill+Goudy&display=swap">
<style>
  :root {
    --paper: #ffffff;
    --ink: #111111;
    --accent: #2a52c9;
    --accent-soft: #8fcaf2;
    --script: "Caveat Brush", cursive;
    --serif: "Sorts Mill Goudy", Georgia, serif;
  }
  * { margin: 0; padding: 0; box-sizing: border-box; }
  html, body {
    width: 1200px; height: 741px; overflow: hidden;
    background: var(--paper);
  }
  .card {
    position: relative;
    width: 1200px; height: 741px;
    background: var(--paper);
    color: var(--ink);
    font-family: var(--serif);
  }
  .practice-mark {
    position: absolute;
    left: 174px; top: 40px;
    width: 220px;
    display: flex; flex-direction: column; align-items: center;
    gap: 18px;
  }
  .practice-mark__dot {
    width: 84px; height: 84px; border-radius: 50%;
    background: var(--accent-soft);
  }
  .practice-mark__name {
    font-family: var(--serif);
    font-size: 26px;
    line-height: 1.15;
    text-align: center;
    color: var(--ink);
  }
  .identity {
    position: absolute;
    left: 393px; top: 232px;
  }
  .identity__name {
    font-family: var(--script);
    font-size: 66px;
    line-height: 1;
    letter-spacing: 1px;
    color: var(--ink);
  }
  .identity__role {
    margin-top: 14px;
    font-family: var(--serif);
    font-size: 28px;
    line-height: 1;
    letter-spacing: 9px;
    text-transform: uppercase;
    font-variant: small-caps;
    color: var(--accent);
  }
  .identity__role .initial { font-size: 39px; }
  .identity__credentials {
    margin-top: 26px;
    font-size: 33px;
    line-height: 1;
    white-space: nowrap;
  }
  .address {
    position: absolute;
    left: 50px; top: 611px;
    font-size: 29px;
    line-height: 52px;
  }
  .contact {
    position: absolute;
    right: 42px; top: 576px;
    font-size: 29px;
    line-height: 46px;
    text-align: left;
  }
  .contact__email { color: var(--accent); }
  .contact__row { word-spacing: 8px; }
</style>
</head>
<body>
  <main class="card">
    <div class="practice-mark">
      <span class="practice-mark__dot"></span>
      <span class="practice-mark__name">Hale Gynaecology</span>
    </div>

    <section class="identity">
      <h1 class="identity__name">Dr. Martin Hale</h1>
      <p class="identity__role"><span class="initial">G</span>ynaecologist</p>
      <p class="identity__credentials">BM BCh, MA (Oxon), Dip Obs, FRANZCOG, MD</p>
    </section>

    <address class="address" style="font-style: normal;">
      Suite # 37, Westbrook Medical Center<br>
      62 Carrow Ave, Elmsford, WA 6012
    </address>

    <div class="contact">
      <div class="contact__email">admin@halegyn.com.au</div>
      <div class="contact__row">Ph: + 6186 -402 -7715</div>
      <div class="contact__row">Fx: + 6186 -402 -7719</div>
    </div>
  </main>
</body>
</html>
```